Boutique town planning business needs a Business Card design

We need a business card design for a new company called The Zoning Bridgeway. We provide town planning and urban design services to government, business and community groups. We would like to see the designs use the colours in the logo (blue, deep red, green and amber), plenty of white and including black and grey in the writing. The final design should communicate collaboration, creativity and professionalism and that we are approachable.

Industry/Entity Type

Town

```html
<!DOCTYPE html>
<html lang="en">
<head>
<meta charset="utf-8">
<title>The Zoning Bridgeway – Business Card</title>
<link rel="stylesheet" href="https://fonts.googleapis.com/css2?family=Open+Sans:wght@400;600;700&family=Libre+Baskerville:wght@700&display=swap">
<style>
  :root {
    --stage: #e6e4e1;
    --card-white: #f7f7f7;
    --card-black: #0d0d0d;
    --ink: #3a3a3a;
    --ink-soft: #6b6b6b;
    --ink-on-dark: #f2f2f2;
    --blue: #3f8fc4;
    --red: #b5342a;
    --green: #6aab3c;
    --amber: #e2a526;
    --ghost: #1e1e1e;
  }
  * { margin: 0; padding: 0; box-sizing: border-box; }
  html, body { width: 1200px; height: 900px; overflow: hidden; }
  body {
    background: var(--stage);
    font-family: "Open Sans", Arial, sans-serif;
    position: relative;
  }
  .card {
    position: absolute;
    width: 560px;
    height: 320px;
    border-radius: 4px;
    box-shadow: 0 8px 24px rgba(0,0,0,0.18);
    overflow: hidden;
  }
  .card--back {
    background: var(--card-black);
    left: 560px;
    top: 90px;
  }
  .card--front {
    background: var(--card-white);
    left: 80px;
    top: 480px;
  }
  .brand {
    position: absolute;
    display: flex;
    align-items: center;
    gap: 12px;
  }
  .brand__dot {
    width: 40px;
    height: 40px;
    border-radius: 50%;
    background: var(--blue);
    flex: none;
  }
  .brand__name {
    font-family: "Open Sans", Arial, sans-serif;
    font-weight: 600;
    font-size: 22px;
    letter-spacing: -0.2px;
  }
  .card--back .brand { left: 60px; top: 40px; }
  .card--back .brand__name { color: var(--ink-on-dark); }
  .card--front .brand { left: 34px; top: 34px; }
  .card--front .brand__name { color: var(--ink); }
  .back-ornament {
    position: absolute;
    right: -70px;
    bottom: -150px;
    width: 360px;
    height: 360px;
    border-radius: 50%;
    background: var(--ghost);
  }
  .contact {
    position: absolute;
    left: 250px;
    top: 150px;
    color: var(--ink-soft);
    font-size: 11.5px;
    line-height: 1.55;
  }
  .contact__name {
    font-family: "Libre Baskerville", Georgia, serif;
    font-weight: 700;
    font-variant: small-caps;
    font-size: 14px;
    letter-spacing: 1px;
    color: var(--ink);
  }
  .contact__role { margin-bottom: 10px; }
  .contact__list { list-style: none; }
  .contact__list li { display: flex; gap: 12px; }
  .contact__label { font-weight: 700; color: var(--ink); width: 12px; }
  .contact__abn { margin-top: 4px; }
</style>
</head>
<body>

  <section class="card card--back" aria-label="Business card, back">
    <div class="back-ornament" aria-hidden="true"></div>
    <div class="brand">
      <span class="brand__dot" aria-hidden="true"></span>
      <span class="brand__name">The Zoning Bridgeway</span>
    </div>
  </section>

  <section class="card card--front" aria-label="Business card, front">
    <div class="brand">
      <span class="brand__dot" aria-hidden="true"></span>
      <span class="brand__name">The Zoning Bridgeway</span>
    </div>
    <div class="contact">
      <p class="contact__name">Marissa Holloway</p>
      <p class="contact__role">BPD (Urban Planning), GDipPD, MPIA, VPELA<br>Director</p>
      <ul class="contact__list">
        <li><span class="contact__label">M</span><span>0400 555 318</span></li>
        <li><span class="contact__label">E</span><span>hello@zoningbridgeway.com.au</span></li>
        <li><span class="contact__label">W</span><span>www.zoningbridgeway.com.au</span></li>
      </ul>
      <p class="contact__abn">ABN 12345678901</p>
    </div>
  </section>

</body>
</html>
```